Door Sticker for Loyalty Rewards App

We need to make stickers that will go on the door of the merchants who are part of the Quiver app.

I have attached the Quiver logo, our colours and examples of other door stickers.

Target Market(s)

Millennials

Colors

Designer to choose colors to be used in the design.

Requirements
Must have
• We would like the Quiver logo as the biggest part of the sticker with the text "Effortless Rewards Available Here" and our URL: www.TrulyQuiverTime.com (you can drop the www if you want).
• Must use the Quiver colours.

```html
<!DOCTYPE html>
<html lang="en">
<head>
<meta charset="utf-8">
<title>Quiver Door Sticker</title>
<link rel="stylesheet" href="https://fonts.googleapis.com/css2?family=Patua+One&family=Arimo:wght@400&display=swap">
<style>
  :root {
    --pink: #ec4c9a;
    --navy: #2e2a6e;
    --blue: #3383c4;
    --purple: #6c58a6;
    --white: #ffffff;
    --frame: #555555;
  }
  html, body {
    margin: 0;
    padding: 0;
    overflow: hidden;
    background: var(--white);
  }
  .sticker {
    position: relative;
    width: 1200px;
    height: 436px;
    box-sizing: border-box;
    border: 1.5px solid var(--frame);
    background: var(--white);
    overflow: hidden;
  }
  .panel {
    position: absolute;
    left: 314px;
    top: 69px;
    width: 830px;
    height: 285px;
    background: var(--pink);
  }
  .panel-inner {
    position: absolute;
    left: 343px;
    top: 85px;
    width: 776px;
    height: 254px;
    background: var(--white);
    overflow: hidden;
  }
  .corner-art {
    position: absolute;
    left: 0;
    top: 0;
    width: 776px;
    height: 254px;
  }
  .badge {
    position: absolute;
    left: 19px;
    top: 63px;
    width: 306px;
    height: 306px;
    box-sizing: border-box;
    border-radius: 50%;
    border: 17px solid var(--pink);
    background: var(--white);
    display: flex;
    align-items: center;
    justify-content: center;
  }
  .brand-name {
    font-family: "Patua One", serif;
    font-size: 64px;
    color: var(--navy);
    line-height: 1;
  }
  .headline {
    position: absolute;
    left: 343px;
    width: 802px;
    margin: 0;
    text-align: center;
    font-family: "Patua One", serif;
    font-weight: 400;
    line-height: 1;
    -webkit-text-stroke: 9px var(--white);
    paint-order: stroke fill;
    white-space: nowrap;
  }
  .headline-top {
    top: 106px;
    font-size: 78px;
    letter-spacing: 2px;
    color: var(--navy);
  }
  .headline-bottom {
    top: 178px;
    font-size: 90px;
    letter-spacing: 5px;
    color: var(--pink);
  }
  .underline {
    position: absolute;
    left: 407px;
    top: 267px;
    width: 675px;
    height: 11px;
    border-radius: 6px;
    background: var(--blue);
    box-shadow: 0 0 0 3px var(--white);
  }
  .url {
    position: absolute;
    left: 343px;
    width: 808px;
    top: 288px;
    margin: 0;
    text-align: center;
    font-family: "Arimo", sans-serif;
    font-size: 35px;
    line-height: 1;
    color: var(--navy);
  }
  .url span {
    background: var(--white);
    padding: 0 4px;
  }
</style>
</head>
<body>
  <div class="sticker">
    <div class="panel"></div>
    <div class="panel-inner">
      <svg class="corner-art" viewBox="0 0 776 254" role="img" aria-label="Decorative corner graphic in brand colours">
        <defs>
          <linearGradient id="cornerFade" x1="0" y1="1" x2="1" y2="0">
            <stop offset="0" stop-color="#3383c4"/>
            <stop offset="0.5" stop-color="#6c58a6"/>
            <stop offset="1" stop-color="#ec4c9a"/>
          </linearGradient>
        </defs>
        <polygon points="549,254 776,254 776,4" fill="url(#cornerFade)"/>
      </svg>
    </div>

    <div class="badge">
      <span class="brand-name">Quiver</span>
    </div>

    <h1 class="headline headline-top">Effortless Rewards</h1>
    <h2 class="headline headline-bottom">Available Here</h2>
    <div class="underline"></div>
    <p class="url"><span>www.TrulyQuiverTime.com</span></p>
  </div>
</body>
</html>
```